WALKING FOOD TOURISM BUSINESS. REQUEST FOR DIGITAL BROCHURE

Our business is a walking food tourism business in and around Melbourne's central city. We are needing a e-digital brochure - to be solely used as email' marketing content, not print. Therefore PDF size needs to be appropriate/suitable. Please see attached written content required for the brochure - together with our logo. For images, I am happy for designer to use our website content (www.wanderplatekitchen.com). OR any other appropriate and creative 'foodie' or Melbourne image suitable. Many thanks:)

Target Market(s)

Premium brand travellers or local adventurous Australians.

Requirements
Must have
• Quality font and images
Nice to have
• Quality Melbourne and food images. See website - wanderplatekitchen.com
Should not have
• Too much colour. Brand is black and white, sophisticated, premium product.

```html
<!DOCTYPE html>
<html lang="en">
<head>
<meta charset="utf-8">
<title>Wanderplate Kitchen Experiences — Brochure</title>
<link rel="stylesheet" href="https://fonts.googleapis.com/css2?family=Montserrat:wght@300;400;500;600;700;800&display=swap">
<style>
  :root {
    --navy: #1b2433;
    --gold: #f2b418;
    --paper: #f6f4ef;
    --ink: #3a3f48;
    --muted: #7b7f87;
    --stage: #e4e4e7;
    --white: #ffffff;
  }
  * { box-sizing: border-box; margin: 0; padding: 0; }
  html, body { width: 900px; height: 1200px; overflow: hidden; }
  body {
    background: var(--stage);
    font-family: "Montserrat", sans-serif;
    color: var(--ink);
    position: relative;
  }
  .spread {
    position: absolute;
    left: 50px;
    width: 800px;
    height: 566px;
    display: flex;
  }
  .spread--outer { top: 20px; }
  .spread--inner { top: 614px; }
  .page {
    position: relative;
    width: 400px;
    height: 566px;
    overflow: hidden;
    background: var(--paper);
  }
  .page + .page { border-left: 1px solid rgba(0,0,0,0.08); }
  .abs { position: absolute; }

  .wordmark {
    font-weight: 600;
    font-size: 15px;
    letter-spacing: 0.5px;
    color: var(--navy);
    display: flex;
    align-items: center;
    gap: 7px;
    white-space: nowrap;
  }
  .wordmark__dot { width: 8px; height: 8px; border-radius: 50%; background: currentColor; }
  .wordmark--light { color: var(--white); }
  .wordmark--small { font-size: 10px; gap: 5px; }
  .wordmark--small .wordmark__dot { width: 6px; height: 6px; }

  /* back page */
  .back { background: var(--navy); color: var(--white); }
  .back__logo { left: 0; right: 0; top: 130px; justify-content: center; }
  .back__heading {
    color: var(--gold);
    font-weight: 700;
    font-size: 13.5px;
    letter-spacing: 0.6px;
    left: 40px;
  }
  .contact {
    left: 40px; top: 210px; width: 320px;
    display: flex; gap: 18px;
    font-size: 9.5px; font-weight: 600;
  }
  .contact__col { display: flex; flex-direction: column; gap: 9px; }
  .contact__divider { width: 1px; background: rgba(255,255,255,0.6); }
  .contact__item { display: flex; align-items: center; gap: 6px; }
  .contact__item svg { width: 9px; height: 9px; }
  .contact__bullet { width: 7px; height: 7px; border-radius: 50%; background: var(--gold); }
  .policy { left: 40px; top: 290px; font-size: 7.8px; line-height: 1.55; color: rgba(255,255,255,0.9); }

  /* cover page */
  .cover__logo { left: 0; right: 0; top: 42px; justify-content: center; }
  .cover__band { left: 0; top: 250px; width: 345px; height: 178px; background: var(--navy); }
  .photo--dining {
    left: 62px; top: 86px; width: 312px; height: 232px;
    background: radial-gradient(circle at 50% 65%, #c9c6bf 0, #8a8479 30%, #4a3f34 62%, #231c17 100%);
  }
  .cover__title {
    left: 38px; top: 334px;
    font-weight: 800; font-size: 21px; letter-spacing: 0.5px;
    color: var(--white); line-height: 1.05;
  }
  .cover__title span {
    display: block; color: var(--gold); font-weight: 400; font-size: 25px; letter-spacing: 1.5px;
  }
  .cover__url { left: 40px; top: 444px; font-weight: 700; font-size: 11.5px; color: var(--navy); letter-spacing: 0.3px; }

  /* inner pages */
  .kicker { left: 40px; top: 26px; font-weight: 700; font-size: 12.5px; letter-spacing: 0.6px; color: var(--navy); }
  .kicker span { color: var(--gold); }
  .photo--group {
    left: 42px; top: 52px; width: 334px; height: 222px;
    background: linear-gradient(160deg, #5f7a3c 0%, #3d5228 35%, #6d5a47 70%, #2a2622 100%);
  }
  .about { left: 0; top: 178px; width: 262px; height: 140px; background: var(--navy); padding: 18px 20px 0 28px; }
  .about__title { font-weight: 700; font-size: 17px; color: var(--gold); margin-bottom: 8px; }
  .about__text { font-size: 7.4px; line-height: 1.6; color: var(--white); }

  .section-title { font-weight: 700; font-size: 11px; letter-spacing: 0.8px; color: var(--navy); }
  .exp-grid { left: 28px; top: 362px; width: 344px; display: flex; gap: 22px; }
  .exp-grid__divider { width: 0; border-left: 1px dashed var(--muted); }
  .exp { width: 150px; }
  .exp__head { display: flex; align-items: center; gap: 7px; margin-bottom: 6px; }
  .icon-badge {
    width: 26px; height: 26px; flex: none; border-radius: 50%;
    background: var(--gold); border: 2px solid var(--navy);
    display: flex; align-items: center; justify-content: center;
  }
  .icon-badge svg { width: 12px; height: 12px; }
  .exp__name { font-weight: 700; font-size: 9.5px; color: var(--navy); line-height: 1.2; }
  .exp__meta { font-weight: 600; font-size: 6.8px; color: var(--gold); margin-bottom: 3px; }
  .exp__text { font-size: 6.8px; line-height: 1.55; color: var(--ink); }

  .page-foot__logo { left: 30px; top: 490px; }
  .page-foot__rule { left: 30px; top: 518px; width: 340px; height: 1px; background: var(--navy); }
  .page-foot__url {
    top: 526px; left: 222px; width: 134px; height: 18px;
    background: var(--gold); color: var(--navy);
    font-weight: 700; font-size: 7.6px;
    display: flex; align-items: center; justify-content: center;
  }
  .page-foot__num {
    top: 524px; left: 352px; width: 22px; height: 22px; border-radius: 50%;
    background: var(--navy); color: var(--white);
    font-weight: 700; font-size: 8px;
    display: flex; align-items: center; justify-content: center;
  }

  .story { left: 30px; top: 38px; width: 188px; height: 152px; background: var(--navy); padding: 16px 16px 0 18px; }
  .story__title { font-weight: 700; font-size: 12px; letter-spacing: 0.8px; color: var(--gold); margin-bottom: 9px; }
  .story__text { font-size: 7px; line-height: 1.6; color: var(--white); }
  .photo--distillery {
    left: 226px; top: 30px; width: 148px; height: 182px;
    background: linear-gradient(170deg, #8c6a4e 0%, #5b4636 45%, #2f2620 100%);
  }
  .tour-list { left: 30px; top: 228px; width: 344px; display: flex; flex-direction: column; gap: 20px; }
  .tour .exp__name { font-size: 10.5px; }
</style>
</head>
<body>

  <section class="spread spread--outer">
    <article class="page back">
      <div class="abs wordmark wordmark--light back__logo"><span class="wordmark__dot"></span>Wanderplate Kitchen</div>
      <h2 class="abs back__heading" style="top:176px;">FOR BOOKING SCHEDULE &amp; ENQUIRY</h2>
      <div class="abs contact">
        <div class="contact__col">
          <div class="contact__item">
            <svg viewBox="0 0 10 10"><path d="M2 1h2l1 2.5-1.2.8a5 5 0 0 0 2 2l.8-1.2L9 6v2a1 1 0 0 1-1 1A7 7 0 0 1 1 2a1 1 0 0 1 1-1z" fill="#f2b418"/></svg>
            +61 400 218 940
          </div>
          <div class="contact__item">
            <svg viewBox="0 0 10 10"><circle cx="5" cy="5" r="4" fill="none" stroke="#f2b418" stroke-width="1.2"/><path d="M1 5h8M5 1c-2 2.5-2 5.5 0 8M5 1c2 2.5 2 5.5 0 8" fill="none" stroke="#f2b418" stroke-width="0.8"/></svg>
            www.wanderplatekitchen.com
          </div>
        </div>
        <div class="contact__divider"></div>
        <div class="contact__col">
          <div class="contact__item"><span class="contact__bullet"></span>wanderplate.kitchen</div>
          <div class="contact__item"><span class="contact__bullet"></span>WanderplateKitchen</div>
        </div>
      </div>
      <h2 class="abs back__heading" style="top:262px;">CANCELLATION &amp; AMENDMENTS</h2>
      <p class="abs policy">100% REFUND for cancellations outside 24 hours of the tour departure time<br>NO REFUND for cancellations made within 24 hours of the tour departure time</p>
    </article>

    <article class="page cover">
      <div class="abs wordmark cover__logo"><span class="wordmark__dot"></span>Wanderplate Kitchen</div>
      <div class="abs cover__band"></div>
      <div class="abs photo--dining" role="img" aria-label="Plated fine-dining dish on a restaurant table with glassware"></div>
      <h1 class="abs cover__title">WANDERPLATE KITCHEN<span>EXPERIENCES</span></h1>
      <p class="abs cover__url">www.wanderplatekitchen.com</p>
    </article>
  </section>

  <section class="spread spread--inner">
    <article class="page">
      <h2 class="abs kicker"><span>WANDERPLATE</span> KITCHEN EXPERIENCES</h2>
      <div class="abs photo--group" role="img" aria-label="Group of guests enjoying food and wine outdoors at a vineyard table"></div>
      <div class="abs about">
        <h3 class="about__title">About Us</h3>
        <p class="about__text">We provide experiential adventure for visitors and locals alike, all through the lens of exceptional food. Our tours capture the essence of Melbourne, its people and diverse history, stopping to sip, savour and delight in the city's foodie hot spots.</p>
      </div>
      <h3 class="abs section-title" style="left:28px; top:338px;">OUR EXPERIENCES</h3>
      <div class="abs exp-grid">
        <div class="exp">
          <div class="exp__head">
            <span class="icon-badge"><svg viewBox="0 0 12 12"><rect x="2" y="4" width="8" height="6" fill="#1b2433"/><path d="M4 4V2h4v2" fill="none" stroke="#1b2433" stroke-width="1.2"/></svg></span>
            <span class="exp__name">Laneway Tasting Trail</span>
          </div>
          <p class="exp__meta">3.5 hours · Midday start</p>
          <p class="exp__text">A curated walk through laneways, markets and hidden kitchens, tasting the city's signature dishes.</p>
        </div>
        <div class="exp-grid__divider"></div>
        <div class="exp">
          <div class="exp__head">
            <span class="icon-badge"><svg viewBox="0 0 12 12"><circle cx="6" cy="6" r="4.5" fill="none" stroke="#1b2433" stroke-width="1.4"/><circle cx="6" cy="6" r="2" fill="#1b2433"/></svg></span>
            <span class="exp__name">Market Bites Walk</span>
          </div>
          <p class="exp__meta">3 hours · Afternoon start</p>
          <p class="exp__text">Bite-sized flavours from street vendors, food trucks and small bars across the central city.</p>
        </div>
      </div>
      <div class="abs wordmark wordmark--small page-foot__logo"><span class="wordmark__dot"></span>Wanderplate Kitchen</div>
      <div class="abs page-foot__rule"></div>
      <div class="abs page-foot__url">www.wanderplatekitchen.com</div>
      <div class="abs page-foot__num">01</div>
    </article>

    <article class="page">
      <div class="abs story">
        <h3 class="story__title">OUR STORY</h3>
        <p class="story__text">Born and raised in Melbourne, with a huge love and passion for everything food, we created these tours to share the city we adore. Walk with us and taste the stories behind every plate.</p>
      </div>
      <div class="abs photo--distillery" role="img" aria-label="Guests at a tasting table inside a copper-still distillery"></div>
      <div class="abs tour-list">
        <div class="tour">
          <div class="exp__head">
            <span class="icon-badge"><svg viewBox="0 0 12 12"><path d="M1 3h4.5v7H1zM6.5 3H11v7H6.5z" fill="#1b2433"/></svg></span>
            <span class="exp__name">Tales of the City Walk</span>
          </div>
          <p class="exp__meta">2.5 hours · Morning start</p>
          <p class="exp__text">Discover the characters, culture and community of our city through laneways, arcades and landmark cafés, tasting local favourites along the way.</p>
        </div>
        <div class="tour">
          <div class="exp__head">
            <span class="icon-badge"><svg viewBox="0 0 12 12"><path d="M3 1h6l-1 4a2 2 0 0 1-4 0zM6 7v3M4 11h4" fill="none" stroke="#1b2433" stroke-width="1.3"/></svg></span>
            <span class="exp__name">Twilight Plates &amp; Pours</span>
          </div>
          <p class="exp__meta">3 hours · Evening start</p>
          <p class="exp__text">Small plates matched with local wines and craft drinks at some of the city's most loved evening venues.</p>
        </div>
        <div class="tour">
          <div class="exp__head">
            <span class="icon-badge"><svg viewBox="0 0 12 12"><path d="M2 8a4 4 0 0 1 8 0zM1 9h10" fill="#1b2433" stroke="#1b2433" stroke-width="1"/><circle cx="6" cy="3" r="0.9" fill="#1b2433"/></svg></span>
            <span class="exp__name">Tailored Group Tables</span>
          </div>
          <p class="exp__meta">Tailored to your group</p>
          <p class="exp__text">Our private tours are ideal for celebrations, team events and special occasions, with menus and routes shaped around your group.</p>
        </div>
      </div>
      <div class="abs wordmark wordmark--small page-foot__logo"><span class="wordmark__dot"></span>Wanderplate Kitchen</div>
      <div class="abs page-foot__rule"></div>
      <div class="abs page-foot__url">www.wanderplatekitchen.com</div>
      <div class="abs page-foot__num">02</div>
    </article>
  </section>

</body>
</html>
```